Looking for a dynamic business card for a pizzeria.

A business card with our food, logo, and space for name, title, email, website, phone. The card should convey quality, unique, amazing. On the front, I envision food photo or photos with the owners names and contact information. On the back, more food with locations, website, facebook, twitter, instagram icons. It should look polished, not cartoonish, or plain.
Target Market(s)
upscale, local food buyers, 30-50 years in age.
Industry/Entity Type
Restaurant
Contact Information for Business Card
Business Name: Crustella, LLC
Website: www.crustellaovens.com
Back:
2 locations: (can list on the back of card)
1. Fairhaven
2736 Marlow Street
Bellingham, WA 98225
360-555-0143
2. Alabama Hill
1187 Pelham Street
Bellingham, WA 98229
360-555-0187
front:
EDITABLE space for
Business name
Person's Name
title
2nd title
Email address
cell-phone number
Requirements
Must have
- logo
- my food photo or photos (no watermarks showing)
- locations on back
- Person contact information on front
- full bleed

```html
<!DOCTYPE html>
<html lang="en">
<head>
<meta charset="utf-8">
<title>Crustella Business Card</title>
<link href="https://fonts.googleapis.com/css2?family=Arimo:wght@700&display=swap" rel="stylesheet">
<style>
  :root {
    --brand-red: #9c3434;
    --brand-red-deep: #8f2e2e;
    --paper: #ffffff;
    --edge: #d9d9d9;
  }
  html, body {
    margin: 0;
    padding: 0;
    overflow: hidden;
    background: var(--paper);
  }
  .card {
    position: relative;
    width: 1200px;
    height: 654px;
    box-sizing: border-box;
    border: 1px solid var(--edge);
    background: var(--paper);
    overflow: hidden;
    font-family: "Arimo", Arial, sans-serif;
    font-weight: 700;
    color: var(--brand-red);
  }

  .photo-band {
    position: absolute;
    left: 34px;
    width: 251px;
    background: linear-gradient(160deg, var(--brand-red) 0%, var(--brand-red-deep) 100%);
  }
  .photo-band--top { top: 0; height: 205px; }
  .photo-band--bottom { top: 449px; bottom: 0; }

  .brand-mark {
    position: absolute;
    left: 113px;
    top: 258px;
    width: 92px;
    height: 92px;
    box-sizing: border-box;
    border: 4px solid var(--brand-red);
    border-radius: 50%;
  }
  .company-name {
    position: absolute;
    left: 34px;
    width: 251px;
    top: 413px;
    margin: 0;
    text-align: center;
    font-size: 30px;
    line-height: 1;
    white-space: nowrap;
  }

  .person {
    position: absolute;
    right: 246px;
    top: 109px;
    text-align: right;
  }
  .person__name {
    margin: 0;
    font-size: 56px;
    line-height: 1;
    white-space: nowrap;
  }
  .person__title {
    margin: 3px 0 0;
    font-size: 25px;
    line-height: 1;
  }

  .contact-icon {
    position: absolute;
    width: 91px;
    height: 91px;
    border-radius: 50%;
    background: var(--brand-red);
    display: flex;
    align-items: center;
    justify-content: center;
  }
  .contact-icon svg { display: block; }
  .contact-icon--address { left: 464px; top: 360px; }
  .contact-icon--phone   { left: 464px; top: 486px; }
  .contact-icon--email   { left: 750px; top: 360px; }
  .contact-icon--web     { left: 750px; top: 486px; }

  .contact-text {
    position: absolute;
    margin: 0;
    font-size: 19px;
    line-height: 24px;
    white-space: nowrap;
  }
  .contact-text--address { left: 564px; top: 379px; }
  .contact-text--phone   { left: 568px; top: 506px; }
  .contact-text--email   { left: 868px; top: 381px; }
  .contact-text--web     { left: 867px; top: 516px; }
</style>
</head>
<body>
  <div class="card">
    <div class="photo-band photo-band--top" role="img" aria-label="Food photo space"></div>
    <div class="photo-band photo-band--bottom" role="img" aria-label="Food photo space"></div>

    <span class="brand-mark" aria-hidden="true"></span>
    <p class="company-name">Crustella</p>

    <div class="person">
      <h1 class="person__name">COMPLETE NAME</h1>
      <p class="person__title">BUSINESS TITLE</p>
    </div>

    <span class="contact-icon contact-icon--address">
      <svg width="36" height="50" viewBox="0 0 36 50" aria-hidden="true">
        <path d="M18 2C9 2 3 8.5 3 17c0 11 15 31 15 31s15-20 15-31C33 8.5 27 2 18 2z" fill="none" stroke="#fff" stroke-width="3"/>
        <circle cx="18" cy="17" r="6" fill="none" stroke="#fff" stroke-width="3"/>
      </svg>
    </span>
    <p class="contact-text contact-text--address">2736 Marlow Street<br>1187 Pelham Street</p>

    <span class="contact-icon contact-icon--phone">
      <svg width="46" height="52" viewBox="0 0 46 52" aria-hidden="true">
        <rect x="3" y="3" width="20" height="34" rx="3" fill="none" stroke="#fff" stroke-width="3"/>
        <rect x="20" y="14" width="22" height="35" rx="3" fill="#9c3434" stroke="#fff" stroke-width="3"/>
        <line x1="26" y1="42" x2="36" y2="42" stroke="#fff" stroke-width="2.5"/>
        <line x1="9" y1="31" x2="16" y2="31" stroke="#fff" stroke-width="2.5"/>
      </svg>
    </span>
    <p class="contact-text contact-text--phone">360-555-0143<br>360-555-0187</p>

    <span class="contact-icon contact-icon--email">
      <svg width="40" height="28" viewBox="0 0 40 28" aria-hidden="true">
        <rect x="2" y="2" width="36" height="24" fill="none" stroke="#fff" stroke-width="3"/>
        <path d="M2 2l18 14L38 2" fill="none" stroke="#fff" stroke-width="3"/>
      </svg>
    </span>
    <p class="contact-text contact-text--email">Email Address @ company.com</p>

    <span class="contact-icon contact-icon--web">
      <svg width="56" height="56" viewBox="0 0 56 56" aria-hidden="true" fill="none" stroke="#fff" stroke-width="3">
        <circle cx="28" cy="28" r="24"/>
        <ellipse cx="28" cy="28" rx="11" ry="24"/>
        <line x1="28" y1="4" x2="28" y2="52"/>
        <line x1="4" y1="28" x2="52" y2="28"/>
        <path d="M8 16h40M8 40h40"/>
      </svg>
    </span>
    <p class="contact-text contact-text--web">www.crustellaovens.com</p>
  </div>
</body>
</html>
```